Plastic Business Card for Bookkeeper

We are looking for a simple professional business card design to use for printing on thin frosted plastic (see-through) card stock. Logo and brand guideline documents are attached as well as a photo of our old business card, and another business card example that we like.

Target Market(s)

Small Business

Industry/Entity Type

Bookkeeper

Contact Information for Business Card

Harriet Olsen CPA
Chief Executive Bookkeeper
T. 03 5926 4417
M. 0438 761 205
E. harriet@pinecrestledger.com
W. www.pinecrestledger.com

Font styles to use
Sans Serif

Colors
6b449b
00a990

Requirements
Must have
• Stick with logo colors. Writing should be clear and easy to read and not too cramped together.
Nice to have
• Tag line for back of the card - 'Not your ordinary Bookkeeper'

```html
<!DOCTYPE html>
<html lang="en">
<head>
<meta charset="utf-8">
<title>Pinecrest Ledger – Business Card</title>
<link rel="stylesheet" href="https://fonts.googleapis.com/css2?family=Montserrat:wght@600&family=Roboto:wght@400;700&display=swap">
<style>
  :root {
    --canvas: #e9eceb;
    --card-white: #ffffff;
    --brand-violet: #4636fc;
    --brand-teal: #1a9687;
    --rule-grey: #a7abad;
    --card-shadow: 0 6px 18px rgba(40, 50, 60, 0.14);
  }
  * { margin: 0; padding: 0; box-sizing: border-box; }
  html, body {
    width: 1200px;
    height: 909px;
    overflow: hidden;
    background: var(--canvas);
  }
  .sheet {
    position: relative;
    width: 1200px;
    height: 909px;
  }
  .card {
    position: absolute;
    top: 290px;
    width: 540px;
    height: 330px;
    box-shadow: var(--card-shadow);
    overflow: hidden;
  }
  .card--front { left: 40px; background: var(--card-white); }
  .card--back { left: 620px; background: var(--brand-violet); }

  /* Front: brand block */
  .brand {
    position: absolute;
    left: 38px;
    top: 112px;
    width: 170px;
    display: flex;
    flex-direction: column;
    align-items: center;
    gap: 12px;
  }
  .brand__dot {
    width: 46px;
    height: 46px;
    border-radius: 50%;
    background: var(--brand-teal);
  }
  .brand__name {
    font-family: "Montserrat", sans-serif;
    font-weight: 600;
    font-size: 16px;
    letter-spacing: 0.4px;
    color: var(--brand-violet);
    text-align: center;
    line-height: 1.2;
  }

  .divider {
    position: absolute;
    left: 210px;
    top: 60px;
  }

  /* Front: person and contacts */
  .person {
    position: absolute;
    left: 318px;
    top: 92px;
    width: 180px;
  }
  .person__name {
    font-family: "Roboto", sans-serif;
    font-weight: 700;
    font-size: 17px;
    color: var(--brand-violet);
  }
  .person__title {
    font-family: "Roboto", sans-serif;
    font-weight: 400;
    font-size: 9.5px;
    color: var(--brand-violet);
    margin-top: 2px;
    padding-bottom: 6px;
    border-bottom: 1px solid var(--rule-grey);
  }
  .contacts {
    list-style: none;
    margin-top: 18px;
  }
  .contacts__item {
    display: flex;
    align-items: center;
    gap: 10px;
    font-family: "Roboto", sans-serif;
    font-size: 12.5px;
    color: var(--brand-teal);
    line-height: 1;
    margin-bottom: 8px;
    white-space: nowrap;
  }
  .contacts__icon { width: 12px; height: 12px; flex: none; }

  /* Back: seal */
  .seal {
    position: absolute;
    left: 50%;
    top: 50%;
    width: 220px;
    height: 220px;
    transform: translate(-50%, -50%);
    border-radius: 50%;
    border: 4px solid var(--card-white);
    display: flex;
    align-items: center;
    justify-content: center;
  }
  .seal__inner {
    width: 198px;
    height: 198px;
    border-radius: 50%;
    background: var(--card-white);
    display: flex;
    flex-direction: column;
    align-items: center;
    justify-content: center;
    gap: 12px;
  }
</style>
</head>
<body>
<main class="sheet">

  <section class="card card--front" aria-label="Business card front">
    <div class="brand">
      <span class="brand__dot"></span>
      <span class="brand__name">PINECREST LEDGER</span>
    </div>

    <svg class="divider" width="80" height="210" viewBox="0 0 80 210" aria-hidden="true">
      <line x1="14" y1="4" x2="56" y2="126" stroke="var(--rule-grey)" stroke-width="1.4"/>
      <line x1="2" y1="60" x2="36" y2="156" stroke="var(--rule-grey)" stroke-width="1.4"/>
      <line x1="30" y1="54" x2="78" y2="200" stroke="var(--rule-grey)" stroke-width="1.4"/>
    </svg>

    <div class="person">
      <p class="person__name">Harriet Olsen CPA</p>
      <p class="person__title">Chief Executive Bookkeeper</p>
      <ul class="contacts">
        <li class="contacts__item">
          <svg class="contacts__icon" viewBox="0 0 12 12" aria-hidden="true">
            <path d="M2.5 1 L4.5 1 L5 3.5 L3.8 4.5 Q4.8 7 7.5 8.2 L8.5 7 L11 7.5 L11 9.5 Q10.5 11 9 11 Q1 9 1 2.5 Q1 1 2.5 1 Z" fill="var(--brand-teal)"/>
          </svg>
          <span>03 5926 4417</span>
        </li>
        <li class="contacts__item">
          <svg class="contacts__icon" viewBox="0 0 12 12" aria-hidden="true">
            <rect x="3" y="0.8" width="6" height="10.4" rx="1" fill="none" stroke="var(--brand-teal)" stroke-width="1.2"/>
            <circle cx="6" cy="9.3" r="0.7" fill="var(--brand-teal)"/>
          </svg>
          <span>0438 761 205</span>
        </li>
        <li class="contacts__item">
          <svg class="contacts__icon" viewBox="0 0 12 12" aria-hidden="true">
            <rect x="0.8" y="2.5" width="10.4" height="7" fill="none" stroke="var(--brand-teal)" stroke-width="1.2"/>
            <path d="M0.8 2.5 L6 6.5 L11.2 2.5" fill="none" stroke="var(--brand-teal)" stroke-width="1.2"/>
          </svg>
          <span>harriet@pinecrestledger.com</span>
        </li>
      </ul>
    </div>
  </section>

  <section class="card card--back" aria-label="Business card back">
    <div class="seal">
      <div class="seal__inner">
        <span class="brand__dot"></span>
        <span class="brand__name">PINECREST LEDGER</span>
      </div>
    </div>
  </section>

</main>
</body>
</html>
```